Higher co-efficient of performance means more heat for your money

I need a bar graph that will have the following heating systems, 80% efficient gas furnace COP of .8, Electric heat COP of 1, and Our best selling heat pump with a cop of 4 at 47F. I will have a constant bar, 100$ worth of gas for furnace, 100$ of electricity for electric heat, and 100$ worth of electricity for our heat pumps. next to them I will have a bar showing how much heat each heating system will provide for $100 of fuel. For gas furnace I need a bar that says $80 worth of heat and the barograph to match it, for electric heat I need the bar to show 100$ worth of heat, for our best selling heat pump I need the bar graph to show and say $400 dollars worth of heat. Please take a look at my website www.brightmarkcomfort.example for brand color and feel

```html
<!DOCTYPE html>
<html lang="en">
<head>
<meta charset="utf-8">
<title>Higher COP Means More Heat For Your Money</title>
<link href="https://fonts.googleapis.com/css2?family=Russo+One&family=Montserrat:wght@600;700;800&display=swap" rel="stylesheet">
<style>
  :root{
    --brand-blue:#1f6fc5;
    --brand-red:#d3282f;
    --panel-tint:#e9f3fc;
    --ink:#111111;
    --rule:#b9b9b9;
    --icon-grey:#c9c9c9;
    --white:#ffffff;
  }
  html,body{margin:0;padding:0;overflow:hidden;background:var(--white);}
  .canvas{width:1200px;height:1200px;position:relative;}
  .canvas svg{display:block;}
  .title{font-family:"Russo One",sans-serif;fill:var(--white);}
  .banner-text{font-family:"Russo One",sans-serif;fill:var(--white);}
  .note{font-family:"Russo One",sans-serif;fill:var(--white);}
  .brand-name{font-family:"Russo One",sans-serif;fill:var(--brand-blue);}
  .value{font-family:"Russo One",sans-serif;font-size:24px;}
  .value--in{fill:var(--brand-blue);}
  .value--out{fill:var(--brand-red);}
  .axis-label{font-family:Montserrat,sans-serif;font-weight:700;font-size:15px;fill:var(--ink);}
  .tag-small{font-family:Montserrat,sans-serif;font-weight:800;font-size:11px;fill:var(--ink);}
  .tag-pct{font-family:"Russo One",sans-serif;font-size:17px;fill:var(--brand-blue);}
  .tag-cop{font-family:"Russo One",sans-serif;font-size:18px;fill:var(--white);}
  .tag-name{font-family:Montserrat,sans-serif;font-weight:800;font-size:17px;fill:var(--white);}
  .pill-num{font-family:"Russo One",sans-serif;font-size:26px;fill:var(--brand-blue);}
  .pill-text{font-family:Montserrat,sans-serif;font-weight:700;font-size:12px;fill:#333;}
  .best-seller{font-family:"Russo One",sans-serif;font-size:22px;fill:var(--white);}
</style>
</head>
<body>
<div class="canvas">
<svg width="1200" height="1200" viewBox="0 0 1200 1200" xmlns="http://www.w3.org/2000/svg">
  <defs>
    <linearGradient id="best-seller-fill" x1="0" x2="1" y1="0" y2="0">
      <stop offset="0" stop-color="#1f6fc5"/>
      <stop offset="0.55" stop-color="#1f6fc5"/>
      <stop offset="1" stop-color="#d3282f"/>
    </linearGradient>
    <linearGradient id="cop-fill" x1="0" x2="1" y1="0" y2="0">
      <stop offset="0" stop-color="#1f6fc5"/>
      <stop offset="1" stop-color="#d3282f"/>
    </linearGradient>
  </defs>

  <!-- heat pump highlight panel -->
  <rect class="panel-highlight" x="800" y="328" width="350" height="616" fill="var(--panel-tint)"/>

  <!-- header band -->
  <path class="header-band" d="M120 166 H1090 A60 60 0 0 1 1150 226 V328 H120 Z" fill="var(--brand-blue)"/>
  <text class="title" x="752" y="207" font-size="28" text-anchor="middle">HIGHER COEFFICIENT OF</text>
  <text class="title" x="752" y="241" font-size="28" text-anchor="middle">PERFORMANCE (COP) MEANS</text>
  <rect class="banner" x="440" y="251" width="572" height="37" fill="var(--brand-red)"/>
  <text class="banner-text" x="726" y="279" font-size="26" text-anchor="middle">MORE HEAT FOR YOUR MONEY!</text>
  <text class="note" x="578" y="313" font-size="17">*COP Measure at 47°C</text>

  <!-- brand seal -->
  <circle class="brand-seal" cx="231" cy="278" r="106" fill="var(--white)" stroke="var(--brand-blue)" stroke-width="3"/>
  <text class="brand-name" x="231" y="272" font-size="25" text-anchor="middle">BRIGHTMARK</text>
  <text class="brand-name" x="231" y="304" font-size="25" text-anchor="middle">COMFORT</text>

  <!-- best seller badge -->
  <rect class="best-seller-badge" x="816" y="335" width="319" height="65" fill="url(#best-seller-fill)"/>
  <text class="best-seller" x="975" y="363" text-anchor="middle">OUR BEST SELLING</text>
  <text class="best-seller" x="975" y="389" text-anchor="middle">HEAT PUMP</text>

  <!-- column dividers -->
  <line x1="450" y1="344" x2="450" y2="944" stroke="var(--rule)" stroke-width="2"/>
  <line x1="800" y1="344" x2="800" y2="944" stroke="var(--rule)" stroke-width="2"/>

  <!-- bars (drawn before axis) -->
  <g class="bars">
    <rect x="207" y="625" width="24" height="110" rx="12" fill="var(--brand-blue)"/>
    <rect x="316" y="648" width="24" height="87" rx="12" fill="var(--brand-red)"/>
    <rect x="557" y="621" width="24" height="114" rx="12" fill="var(--brand-blue)"/>
    <rect x="667" y="621" width="24" height="114" rx="12" fill="var(--brand-red)"/>
    <rect x="909" y="621" width="24" height="114" rx="12" fill="var(--brand-blue)"/>
    <rect x="1019" y="416" width="24" height="319" rx="12" fill="var(--brand-red)"/>
  </g>

  <!-- axis -->
  <line class="axis" x1="116" y1="733" x2="1140" y2="733" stroke="var(--brand-blue)" stroke-width="3"/>
  <circle cx="116" cy="733" r="7" fill="var(--brand-blue)"/>
  <circle cx="1140" cy="733" r="7" fill="var(--brand-blue)"/>

  <!-- bulbs with icons -->
  <g class="bulbs">
    <!-- gas -->
    <circle cx="219" cy="731" r="31" fill="var(--brand-blue)"/>
    <rect x="208" y="720" width="22" height="26" rx="7" fill="var(--white)"/>
    <rect x="214" y="713" width="10" height="7" rx="2" fill="var(--white)"/>
    <!-- heat thermometers -->
    <circle cx="328" cy="731" r="31" fill="var(--brand-red)"/>
    <rect x="324" y="712" width="8" height="26" rx="4" fill="var(--white)"/>
    <circle cx="328" cy="742" r="7" fill="var(--white)"/>
    <circle cx="679" cy="731" r="31" fill="var(--brand-red)"/>
    <rect x="675" y="712" width="8" height="26" rx="4" fill="var(--white)"/>
    <circle cx="679" cy="742" r="7" fill="var(--white)"/>
    <circle cx="1031" cy="731" r="31" fill="var(--brand-red)"/>
    <rect x="1027" y="712" width="8" height="26" rx="4" fill="var(--white)"/>
    <circle cx="1031" cy="742" r="7" fill="var(--white)"/>
    <!-- electricity -->
    <circle cx="569" cy="731" r="31" fill="var(--brand-blue)"/>
    <circle cx="569" cy="731" r="17" fill="none" stroke="var(--white)" stroke-width="3"/>
    <path d="M572 718 L562 733 H569 L566 745 L577 728 H570 Z" fill="var(--white)"/>
    <circle cx="921" cy="731" r="31" fill="var(--brand-blue)"/>
    <circle cx="921" cy="731" r="17" fill="none" stroke="var(--white)" stroke-width="3"/>
    <path d="M924 718 L914 733 H921 L918 745 L929 728 H922 Z" fill="var(--white)"/>
  </g>

  <!-- values -->
  <text class="value value--in" x="192" y="648" text-anchor="end">100</text>
  <text class="value value--out" x="350" y="665">80</text>
  <text class="value value--in" x="545" y="645" text-anchor="end">100</text>
  <text class="value value--out" x="700" y="645">100</text>
  <text class="value value--in" x="897" y="643" text-anchor="end">100</text>
  <text class="value value--out" x="1052" y="437">400</text>

  <!-- axis labels -->
  <text class="axis-label" x="219" y="780" text-anchor="middle">GAS</text>
  <text class="axis-label" x="328" y="780" text-anchor="middle">HEAT</text>
  <text class="axis-label" x="569" y="780" text-anchor="middle">ELECTRICITY</text>
  <text class="axis-label" x="679" y="780" text-anchor="middle">HEAT</text>
  <text class="axis-label" x="921" y="780" text-anchor="middle">ELECTRICITY</text>
  <text class="axis-label" x="1031" y="780" text-anchor="middle">HEAT</text>

  <!-- system icons (placeholders) -->
  <rect x="155" y="828" width="82" height="80" rx="6" fill="var(--icon-grey)" role="img" aria-label="Gas furnace icon"/>
  <rect x="508" y="833" width="72" height="76" rx="6" fill="var(--icon-grey)" role="img" aria-label="Electric heater icon"/>
  <circle cx="872" cy="868" r="36" fill="#c9dcef"/>

  <!-- spec tags -->
  <g class="spec-tag">
    <rect x="250" y="816" width="160" height="106" fill="var(--white)" stroke="var(--brand-blue)" stroke-width="2"/>
    <rect x="330" y="816" width="80" height="48" fill="var(--brand-blue)"/>
    <text class="tag-pct" x="256" y="838">80%</text>
    <text class="tag-small" x="256" y="856">EFFICIENT</text>
    <text class="tag-cop" x="370" y="847" text-anchor="middle">COP 0.8</text>
    <rect x="250" y="864" width="160" height="58" fill="var(--ink)"/>
    <text class="tag-name" x="330" y="899" text-anchor="middle">GAS FURNACE</text>
  </g>
  <g class="spec-tag">
    <rect x="600" y="816" width="160" height="106" fill="var(--white)" stroke="var(--brand-blue)" stroke-width="2"/>
    <rect x="680" y="816" width="80" height="48" fill="var(--brand-blue)"/>
    <text class="tag-pct" x="606" y="838">100%</text>
    <text class="tag-small" x="606" y="856">EFFICIENT</text>
    <text class="tag-cop" x="720" y="847" text-anchor="middle">COP 1</text>
    <rect x="600" y="864" width="160" height="58" fill="var(--ink)"/>
    <text class="tag-name" x="680" y="889" text-anchor="middle">ELECTRIC</text>
    <text class="tag-name" x="680" y="911" text-anchor="middle">HEATER</text>
  </g>
  <g class="spec-tag">
    <rect x="948" y="816" width="160" height="106" fill="var(--white)" stroke="var(--brand-blue)" stroke-width="2"/>
    <rect x="1028" y="816" width="80" height="48" fill="url(#cop-fill)"/>
    <text class="tag-pct" x="954" y="838" style="fill:var(--brand-red)">400%</text>
    <text class="tag-small" x="954" y="856">EFFICIENT</text>
    <text class="tag-cop" x="1068" y="847" text-anchor="middle">COP 4</text>
    <rect x="948" y="864" width="160" height="58" fill="var(--ink)"/>
    <text class="tag-name" x="1028" y="889" text-anchor="middle">OUR</text>
    <text class="tag-name" x="1028" y="911" text-anchor="middle">HEAT PUMP</text>
  </g>

  <!-- footer cost band -->
  <rect class="cost-band" x="119" y="944" width="1031" height="78" fill="var(--brand-blue)"/>
  <g class="cost-pill">
    <rect x="135" y="960" width="287" height="48" rx="24" fill="var(--white)"/>
    <circle cx="162" cy="984" r="18" fill="var(--brand-blue)"/>
    <text x="162" y="992" font-family="Russo One, sans-serif" font-size="22" fill="#fff" text-anchor="middle">$</text>
    <text class="pill-num" x="190" y="994">100</text>
    <text class="pill-text" x="268" y="980">WORTH OF GAS</text>
    <text class="pill-text" x="268" y="995">FOR FURNACE</text>
  </g>
  <g class="cost-pill">
    <rect x="486" y="960" width="287" height="48" rx="24" fill="var(--white)"/>
    <circle cx="513" cy="984" r="18" fill="var(--brand-blue)"/>
    <text x="513" y="992" font-family="Russo One, sans-serif" font-size="22" fill="#fff" text-anchor="middle">$</text>
    <text class="pill-num" x="541" y="994">100</text>
    <text class="pill-text" x="619" y="972">WORTH OF</text>
    <text class="pill-text" x="619" y="986">ELECTRICITY FOR</text>
    <text class="pill-text" x="619" y="1000">ELECTRIC HEATER</text>
  </g>
  <g class="cost-pill">
    <rect x="835" y="960" width="287" height="48" rx="24" fill="var(--white)"/>
    <circle cx="862" cy="984" r="18" fill="var(--brand-blue)"/>
    <text x="862" y="992" font-family="Russo One, sans-serif" font-size="22" fill="#fff" text-anchor="middle">$</text>
    <text class="pill-num" x="890" y="994">100</text>
    <text class="pill-text" x="968" y="972">WORTH OF</text>
    <text class="pill-text" x="968" y="986">ELECTRICITY FOR</text>
    <text class="pill-text" x="968" y="1000">HEAT PUMP</text>
  </g>
</svg>
</div>
</body>
</html>
```